A new company focused on starting and investing in transformative businesses.

We need a simple and clean website with a few pages. we like larkmeadow.com as a starting point. we want the landing page to be very simple with an option to click through on the top right into INVESTOR LOGIN. then we want to be able to scroll down to see more about our company.

Target Market(s)

professional

Coding

Coded - Design and coding required

Number of Pages Required

2 page

Font styles to use
Serif
Sans Serif

Requirements
Must have
• HALVERN BUILDERS logo (attached as a file) on the top with INVESTOR LOGIN as a click through on the right. Please model the click through from larkmeadow.com. The description (also written in attached file) should be on the landing page. we do not want to have to scroll to read the description.

Then we can scroll down to read more about Halvern including the mission and the two types of businesses. More is detailed on the attached file called "Halvern Website Syntax"
Should not have
• should not be slow loading with lots of fancy graphics. should not be busy and with too many colors.

```html
<!DOCTYPE html>
<html lang="en">
<head>
<meta charset="utf-8">
<title>Halvern Builders</title>
<link rel="stylesheet" href="https://fonts.googleapis.com/css2?family=Montserrat:wght@500;600&family=Mulish:wght@400;800&family=Roboto:wght@400;500;700&display=swap">
<style>
:root{
  --brand:#0b56a0;
  --brand-text:#0d5ba6;
  --ink:#1d1d1f;
  --body:#3b3b3b;
  --muted:#777;
  --hero-a:#f1f1f1;
  --hero-b:#e3e3e3;
  --rule:#e6e6e6;
  --footer:#222022;
}
*{box-sizing:border-box;margin:0;padding:0}
html,body{width:1071px;height:1200px;overflow:hidden;background:#fff}
body{position:relative;font-family:"Mulish",sans-serif;color:var(--body)}
.hero{position:absolute;left:0;top:0;width:1071px;height:422px;
  background:linear-gradient(135deg,var(--hero-a) 0%,var(--hero-b) 45%,#f0f0f0 70%,var(--hero-b) 100%)}
.brand{position:absolute;left:144px;top:28px;display:flex;align-items:center;gap:10px}
.brand-mark{width:44px;height:62px;background:var(--brand)}
.brand-name{font-family:"Roboto",sans-serif;font-weight:500;font-size:24px;line-height:27px;color:#2a2a2a;letter-spacing:.5px}
.login{position:absolute;left:778px;top:38px;width:149px;height:41px;background:var(--brand);border-radius:3px;
  color:#fff;font-family:"Roboto",sans-serif;font-weight:700;font-size:12.5px;display:flex;align-items:center;justify-content:center;letter-spacing:.2px}
.headline{position:absolute;left:266px;top:190px;width:600px;text-align:center;font-family:"Montserrat",sans-serif;
  font-weight:600;font-size:27px;line-height:40px;color:var(--ink);letter-spacing:.6px}
.mission{position:absolute;left:140px;top:482px;width:791px;text-align:center;font-size:20px;line-height:30px;color:var(--brand-text)}
.mission strong{font-weight:800}
.service{position:absolute;top:578px;width:350px}
.service.left{left:145px}
.service.right{left:579px}
.service-head{display:flex;align-items:center;gap:10px;height:38px}
.service-head h3{font-family:"Roboto",sans-serif;font-weight:700;font-size:19px;color:var(--ink)}
.service p{margin-top:15px;font-size:11.6px;line-height:18px;color:var(--body)}
.divider{position:absolute;left:535px;top:562px;width:1px;height:148px;background:var(--rule)}
.team-title{position:absolute;left:0;top:772px;width:1071px;text-align:center;font-family:"Roboto",sans-serif;font-size:23px;color:var(--ink)}
.team-title b{font-weight:700}
.team-rule{position:absolute;left:516px;top:809px;width:39px;height:2px;background:var(--brand)}
.member{position:absolute;top:839px;width:184px;text-align:center}
.portrait{position:relative;width:184px;height:209px;border-radius:3px}
.member h4{margin-top:17px;font-family:"Roboto",sans-serif;font-weight:700;font-size:16px;letter-spacing:.6px;color:var(--ink)}
.member.active h4{color:var(--brand-text)}
.member p{margin-top:4px;font-size:13px;color:var(--muted)}
.member.active p{color:var(--ink)}
.social{position:absolute;left:15px;top:14px;display:flex;flex-direction:column;gap:8px}
.social span{width:24px;height:23px;display:block}
.footer{position:absolute;left:0;top:1157px;width:1071px;height:43px;background:var(--footer);color:#e8e8e8;
  font-size:12px;display:flex;align-items:center;justify-content:center}
.footer b{font-weight:800;margin:0 3px}
</style>
</head>
<body>
<header class="hero" role="img" aria-label="Soft grey background with a faint hexagon pattern">
  <div class="brand"><span class="brand-mark"></span><span class="brand-name">HALVERN<br>BUILDERS</span></div>
  <a class="login">INVESTOR LOGIN</a>
  <h1 class="headline">Halvern Builders Is An Entrepreneurial Firm Focused On Building And Growing Transformational Companies</h1>
</header>

<p class="mission">Our mission is to build <strong>meaningful</strong> businesses that create <strong>enduring</strong> value by impacting people in a <strong>measurable</strong> way.</p>

<section class="service left">
  <div class="service-head">
    <svg width="38" height="38" viewBox="0 0 38 38" fill="none" stroke="#0b56a0" stroke-width="1.4">
      <path d="M3 7h7M3 10h7M3 13h5"/>
      <rect x="5" y="27" width="4" height="7"/><rect x="11" y="24" width="4" height="10"/>
      <rect x="17" y="20" width="4" height="14"/><rect x="23" y="15" width="4" height="19"/><rect x="29" y="9" width="4" height="25"/>
      <path d="M1 36h36M4 24 20 14l10-10M26 4h5v5"/>
    </svg>
    <h3>GROUND UP</h3>
  </div>
  <p>Our ground up business applies a proven analytic process to identify value edge, a form of competitive advantage. We architect transformational companies and are deliberate in creating the foundation necessary to lead an industry.</p>
</section>

<div class="divider"></div>

<section class="service right">
  <div class="service-head">
    <svg width="38" height="38" viewBox="0 0 38 38" fill="none" stroke="#0b56a0" stroke-width="1.4">
      <circle cx="22" cy="9" r="7"/>
      <path d="M24 6h-3a1.5 1.5 0 0 0 0 3h2a1.5 1.5 0 0 1 0 3h-3M22 4v1.5M22 12v1.5"/>
      <path d="M2 30l6 6 4-4M8 24l6-4h8a2 2 0 0 1 0 4h-6M20 24l9-4a2 2 0 0 1 2 3l-10 7H12"/>
    </svg>
    <h3>SPECIAL OPPORTUNITIES</h3>
  </div>
  <p>We partner with exceptional teams that create value by transforming lives. Our investment focus includes large companies and spin-outs.</p>
</section>

<h2 class="team-title"><b>HALVERN</b> BUILDERS</h2>
<div class="team-rule"></div>

<article class="member" style="left:144px">
  <div class="portrait" role="img" aria-label="Portrait photo of Owen Marsh" style="background:linear-gradient(180deg,#e2e2e2,#c9c9cb)"></div>
  <h4>OWEN MARSH</h4><p>Co Founder</p>
</article>
<article class="member active" style="left:343px">
  <div class="portrait" role="img" aria-label="Portrait photo of Clara Dunn" style="background:linear-gradient(180deg,#8a7f89,#5b5158)">
    <div class="social"><span style="background:#0b56a0"></span><span style="background:#12b9e0"></span><span style="background:#0a8fc7"></span></div>
  </div>
  <h4>CLARA DUNN</h4><p>General Manager</p>
</article>
<article class="member" style="left:543px">
  <div class="portrait" role="img" aria-label="Portrait photo of Theo Larkin" style="background:linear-gradient(180deg,#e4e5ef,#cfd0da)"></div>
  <h4>THEO LARKIN</h4><p>Senior Designer</p>
</article>
<article class="member" style="left:743px">
  <div class="portrait" role="img" aria-label="Portrait photo of Ivy Calder" style="background:linear-gradient(180deg,#bcbcbc,#9c9c9c)"></div>
  <h4>IVY CALDER</h4><p>Marketing Manager</p>
</article>

<footer class="footer">Copyright © 2021 <b>HALVERN BUILDERS.</b> All Rights Reserved.</footer>
</body>
</html>
```